This is a label for a new sake made in Japan imported into Aust

This will be a bottle label for a new sake imported into Australia. The hero of the label is the Velmora. We have joined the "O" meaning great in Japanese and used sake with "Z" to have Velmora with the play on words using Oz as in our slang for Aussie. A modern label with a Japanese take is key. This is a premium sake made in Japan for the Australian market.
The "Tall Casks" up the top is the name of the company, we have yet to design a logo for the company.

Target Market(s)

Alcohol

Logo Text

Velmora

Font styles to use
Serif

Requirements
Must have
• easy to read, with a hint of Japanese origin
Should not have
• too busy

```html
<!DOCTYPE html>
<html lang="en">
<head>
<meta charset="UTF-8">
<title>Velmora – Sake Label Colourways</title>
<link href="https://fonts.googleapis.com/css2?family=Arimo:wght@400&display=swap" rel="stylesheet">
<style>
  :root {
    --page-bg: #f4f4f4;
    --band-grey: #a3a3a3;
    --label-border: #1c1c1c;

    --classic-bg: #ffffff;
    --classic-rule: #7a1a1a;
    --classic-dot: #e6a3ab;
    --classic-mark: #1e1e1e;
    --classic-small: #555555;

    --night-bg: #000000;
    --night-rule: #8c1a1c;
    --night-dot: #8c1a1c;
    --night-mark: #e2e2e2;
    --night-small: #bdbdbd;

    --amber-bg: #ffffff;
    --amber-rule: #8a5a22;
    --amber-dot: #e4be8a;
    --amber-mark: #7e4f1a;
    --amber-small: #c99a62;
  }
  * { margin: 0; padding: 0; box-sizing: border-box; }
  html, body { width: 1200px; height: 1000px; overflow: hidden; }
  body { background: var(--page-bg); position: relative; font-family: "Arimo", Arial, sans-serif; }

  .band {
    position: absolute; left: 0; top: 116px;
    width: 1200px; height: 189px;
    background: var(--band-grey);
  }

  .label {
    position: absolute; top: 57px;
    width: 270px; height: 308px;
    border: 1px solid var(--label-border);
    overflow: hidden;
  }
  .label--classic { left: 100px; background: var(--classic-bg);
    --rule: var(--classic-rule); --dot: var(--classic-dot); --mark: var(--classic-mark); --small: var(--classic-small); }
  .label--night { left: 468px; background: var(--night-bg);
    --rule: var(--night-rule); --dot: var(--night-dot); --mark: var(--night-mark); --small: var(--night-small); }
  .label--amber { left: 834px; background: var(--amber-bg);
    --rule: var(--amber-rule); --dot: var(--amber-dot); --mark: var(--amber-mark); --small: var(--amber-small); }

  .rule {
    position: absolute; left: 32px; top: 0; bottom: 0; width: 2px;
    background: var(--rule);
  }

  .company {
    position: absolute; left: 0; right: 0; top: 100px;
    text-align: center;
    font-size: 9px; letter-spacing: 1px;
    color: var(--small);
  }

  .brand {
    position: absolute; left: 48px; top: 128px;
    display: flex; align-items: center; gap: 10px;
  }
  .brand__dot {
    width: 14px; height: 14px; border-radius: 50%;
    background: var(--dot); flex: none;
  }
  .brand__name {
    font-size: 32px; font-weight: 400; line-height: 1;
    letter-spacing: 2px;
    color: var(--mark);
    white-space: nowrap;
  }

  .descriptor {
    position: absolute; right: 24px; top: 180px;
    text-align: right;
    font-size: 9px; line-height: 9px; letter-spacing: 1px;
    color: var(--small);
  }
</style>
</head>
<body>
  <div class="band"></div>

  <section class="label label--classic">
    <span class="rule"></span>
    <p class="company">Tall Casks</p>
    <div class="brand"><span class="brand__dot"></span><h1 class="brand__name">VELMORA</h1></div>
    <p class="descriptor">Premium<br>Japanese<br>Sake</p>
  </section>

  <section class="label label--night">
    <span class="rule"></span>
    <p class="company">Tall Casks</p>
    <div class="brand"><span class="brand__dot"></span><h2 class="brand__name">VELMORA</h2></div>
    <p class="descriptor">Premium<br>Japanese<br>Sake</p>
  </section>

  <section class="label label--amber">
    <span class="rule"></span>
    <p class="company">Tall Casks</p>
    <div class="brand"><span class="brand__dot"></span><h2 class="brand__name">VELMORA</h2></div>
    <p class="descriptor">Premium<br>Japanese<br>Sake</p>
  </section>
</body>
</html>
```